Business Card - The Harborline Group

We need a business card for a new venture capital fund and innovation accelerator based in San Francisco, CA. The Harborline Group will back, fund and scale life-transforming businesses. We intend to provide capital along with strategic and tactical direction to teams running exponential organizations. We are backing great ideas for vast markets with passionate visionaries. We facilitate the rapid creation of life-transforming businesses, help invent or re-invent critical industries and move the frontier of progress for the good of humankind. Maplecrest University defines Exponential Organizations as those whose impact (cost reduction or output) is disproportionally large – at least 10x larger – compared to its peers because of the use of new organizational techniques that leverage accelerating technologies. ExOs are characterized by a massive transformative purpose (MTP), a skunkworks organization and passionate teams of brilliant mountain-climbers with technical backgrounds.

Industry/Entity Type

Business

Contact Information for Business Card

Peter Odell
Managing Director

peter@theharborlinegroup.com
+1.628.307.4190

Font styles to use
Sans Serif

Requirements
Must have
• - logo
• - website: www.theharborlinegroup.com

```html
<!DOCTYPE html>
<html lang="en">
<head>
<meta charset="utf-8">
<title>The Harborline Group – Business Card</title>
<link rel="stylesheet" href="https://fonts.googleapis.com/css2?family=Exo+2:wght@400;600;700;800&display=swap">
<style>
  :root {
    --bg: #e9e8e6;
    --card: #f5f5f4;
    --ink: #3a3a3a;
    --ink-soft: #555555;
    --blue: #124a8c;
    --green: #5aa83f;
    --faint: #e6e6e6;
  }
  * { box-sizing: border-box; margin: 0; padding: 0; }
  html, body { width: 1200px; height: 768px; overflow: hidden; }
  body {
    background: var(--bg);
    font-family: "Exo 2", sans-serif;
    position: relative;
  }
  .card {
    position: absolute;
    width: 540px;
    height: 309px;
    background: var(--card);
    box-shadow: 0 6px 20px rgba(0,0,0,0.12);
    overflow: hidden;
  }
  .card--front { left: 40px; top: 130px; }
  .card--back  { left: 620px; top: 330px; }

  /* brand lockup */
  .brand { position: absolute; display: flex; flex-direction: column; }
  .brand__row { display: flex; align-items: center; gap: 14px; }
  .brand__mark { border-radius: 50%; background: var(--blue); flex: none; }
  .brand__name {
    font-weight: 800;
    color: var(--ink);
    text-transform: uppercase;
    line-height: 1.05;
  }
  .brand__rule { height: 1px; background: var(--ink); }
  .brand__tagline {
    font-weight: 600;
    color: var(--ink);
    text-transform: uppercase;
    letter-spacing: 0.02em;
    line-height: 1.25;
    white-space: nowrap;
  }

  .card--front .brand { left: 70px; top: 90px; width: 400px; }
  .card--front .brand__mark { width: 64px; height: 64px; }
  .card--front .brand__name { font-size: 34px; }
  .card--front .brand__rule { margin: 10px 0 8px 78px; }
  .card--front .brand__tagline { font-size: 10.5px; margin-left: 78px; }

  /* back */
  .band {
    position: absolute; left: 0; top: 0; bottom: 0; width: 34px;
    background: var(--blue);
    border-right: 4px solid var(--green);
  }
  .card--back .brand { left: 92px; top: 40px; width: 260px; }
  .card--back .brand__mark { width: 36px; height: 36px; }
  .card--back .brand__row { gap: 10px; }
  .card--back .brand__name { font-size: 19px; }
  .card--back .brand__rule { margin: 6px 0 5px 46px; }
  .card--back .brand__tagline { font-size: 6.5px; margin-left: 46px; }

  .decoration {
    position: absolute; right: -40px; top: 120px; width: 260px; height: 230px;
    border-radius: 50%;
    background: radial-gradient(circle at 50% 50%, var(--faint) 0%, rgba(230,230,230,0) 70%);
  }
  .person { position: absolute; right: 34px; top: 150px; text-align: right; }
  .person__name { font-size: 18px; font-weight: 700; color: var(--blue); }
  .person__title { font-size: 13px; color: var(--ink-soft); margin-top: 4px; }

  .contacts { position: absolute; left: 64px; bottom: 30px; list-style: none; }
  .contacts li {
    display: flex; align-items: center; gap: 12px;
    font-size: 15px; color: var(--ink); line-height: 26px;
  }
  .contacts svg { width: 12px; height: 12px; fill: var(--blue); flex: none; }
</style>
</head>
<body>

  <section class="card card--front">
    <div class="brand">
      <div class="brand__row">
        <span class="brand__mark"></span>
        <span class="brand__name">The Harborline Group</span>
      </div>
      <div class="brand__rule"></div>
      <p class="brand__tagline">Capital partner and growth studio<br>for breakthrough ventures</p>
    </div>
  </section>

  <section class="card card--back">
    <div class="band"></div>
    <div class="decoration" role="img" aria-label="Faint background decoration"></div>

    <div class="brand">
      <div class="brand__row">
        <span class="brand__mark"></span>
        <span class="brand__name">The Harborline Group</span>
      </div>
      <div class="brand__rule"></div>
      <p class="brand__tagline">Capital partner and growth studio<br>for breakthrough ventures</p>
    </div>

    <div class="person">
      <p class="person__name">Peter Odell</p>
      <p class="person__title">Managing Director</p>
    </div>

    <ul class="contacts">
      <li>
        <svg viewBox="0 0 12 12" aria-hidden="true"><path d="M2 1h2.5l1 3-1.5 1a7 7 0 0 0 3 3l1-1.5 3 1V10a1 1 0 0 1-1 1A9 9 0 0 1 1 2a1 1 0 0 1 1-1z"/></svg>
        +1.628.307.4190
      </li>
      <li>
        <svg viewBox="0 0 12 12" aria-hidden="true"><path d="M0 2h12v8H0z M0 2l6 5 6-5" stroke="#f5f5f4" stroke-width="1"/></svg>
        peter@theharborlinegroup.com
      </li>
      <li>
        <svg viewBox="0 0 12 12" aria-hidden="true"><circle cx="6" cy="6" r="5.5"/><path d="M0.5 6h11M6 0.5c-3 3-3 8 0 11M6 0.5c3 3 3 8 0 11" stroke="#f5f5f4" stroke-width="0.8" fill="none"/></svg>
        www.theharborlinegroup.com
      </li>
    </ul>
  </section>

</body>
</html>
```